Business Card Design

Take existing logo/brand and develop business card for sales team.
We have two separate brands and require a business card for each.

1. VoxHarbor
2. Tallowgate

Refer to our websites www.voxharbor.example.au and www.mynimbuslinko.example.au for designs currently implemented and in the marketplace.

Both cards are brands of our parent company Quorra Systems Pty Ltd - an Australian Telecommunications company in the medium business sector. We have only business customers, no retail/residential consumers.

Target Market(s)

Australian Business - small to medium enterprise

Industry/Entity Type

Business

Contact Information for Business Card

Lev Dorrit
Sales Director
Mobile: +61 400 555 187
Direct: +61 3 9555 0137
Email: lev@voxharbor.example.au
VoxHarbor (a brand of Quorra Systems Pty Ltd)

Lev Dorrit
Sales Director
Mobile: +61 400 555 187
Direct: +61 3 9555 0137
Email: lev@tallowgate.example.au
Tallowgate (a brand of Quorra Systems Pty Ltd)

Font styles to use
Sans Serif
Other font styles liked:
• Roboto Condensed, Open Sans

Requirements
Must have
• Clean lines, crisp fonts - suggest Roboto Condensed or similar.
• Must be easy to read and clear.
• Brand colour #0C8CCD
• Two colour maximum
Nice to have
• Modern, intellectual and unique design.
Should not have
• No die cuts
• No copies or rip-offs of other designs

```html
<!DOCTYPE html>
<html lang="en">
<head>
<meta charset="utf-8">
<title>VoxHarbor and Tallowgate business cards</title>
<link rel="stylesheet" href="https://fonts.googleapis.com/css2?family=Open+Sans:wght@400;600;700&display=swap">
<style>
  :root {
    --brand-blue: #0c6fbf;
    --brand-blue-light: #0c8ccd;
    --ink-dark: #2b2b2e;
    --ink-panel: #333538;
    --paper: #ffffff;
    --backdrop: #e6e9ec;
    --clear-card: rgba(255,255,255,0.55);
    --muted-white: rgba(255,255,255,0.85);
  }
  * { margin: 0; padding: 0; box-sizing: border-box; }
  html, body { width: 1200px; height: 485px; overflow: hidden; }
  body {
    background: var(--backdrop);
    font-family: "Open Sans", Arial, sans-serif;
    position: relative;
  }
  .card {
    position: absolute;
    width: 430px;
    height: 238px;
    overflow: hidden;
  }
  .card--vox { left: 86px; top: 136px; background: var(--brand-blue); }
  .card--tallow {
    left: 686px; top: 136px;
    background: var(--clear-card);
    border: 1px solid rgba(120,130,140,0.45);
  }
  .card__art { position: absolute; left: 0; top: 0; }
  .holder { position: absolute; color: var(--paper); }
  .holder__name { font-weight: 700; font-size: 17px; line-height: 1.1; }
  .holder__title { font-size: 11px; line-height: 1.3; }
  .card--vox .holder { left: 21px; top: 52px; color: var(--muted-white); }
  .card--tallow .holder { right: 238px; top: 148px; text-align: right; }
  .contacts { position: absolute; list-style: none; color: var(--paper); font-size: 11px; line-height: 14px; }
  .contacts li { display: flex; align-items: center; gap: 5px; white-space: nowrap; }
  .contacts svg { width: 9px; height: 9px; flex: none; fill: currentColor; }
  .card--vox .contacts { left: 21px; top: 161px; color: var(--muted-white); }
  .card--tallow .contacts { left: 240px; top: 138px; font-size: 10.5px; }
  .brand {
    position: absolute; display: flex; align-items: center; gap: 8px;
    font-weight: 600;
  }
  .brand--vox { left: 200px; top: 94px; color: var(--brand-blue); font-size: 31px; }
  .brand--vox .brand__dot { width: 18px; height: 18px; border-radius: 50%; background: var(--brand-blue); }
  .brand--tallow { left: 0; right: 0; top: 38px; justify-content: center; color: var(--ink-dark); font-size: 28px; }
  .brand--tallow .brand__square { width: 30px; height: 30px; background: var(--brand-blue-light); }
</style>
</head>
<body>

<section class="card card--vox" aria-label="VoxHarbor business card">
  <svg class="card__art" width="430" height="238" viewBox="0 0 430 238" aria-hidden="true">
    <ellipse cx="294" cy="112" rx="124" ry="106" fill="#ffffff"/>
  </svg>
  <div class="brand brand--vox"><span class="brand__dot"></span><span>VoxHarbor</span></div>
  <div class="holder">
    <p class="holder__name">Lev Dorrit</p>
    <p class="holder__title">Sales Director</p>
  </div>
  <ul class="contacts">
    <li><svg viewBox="0 0 10 10"><rect x="2.5" y="0.5" width="5" height="9" rx="1" fill="none" stroke="currentColor"/></svg>+61 400 555 187</li>
    <li><svg viewBox="0 0 10 10"><path d="M1 3c0-1 1-2 4-2s4 1 4 2v1H7V3H3v1H1zM2 5h6l1 4H1z"/></svg>+61 3 9555 0137</li>
    <li><svg viewBox="0 0 10 10"><path d="M0 2h10v6H0zM0.8 2.6 5 5.6l4.2-3" fill="none" stroke="currentColor"/></svg>lev@voxharbor.example.au</li>
    <li><svg viewBox="0 0 10 10"><circle cx="5" cy="5" r="4.4" fill="none" stroke="currentColor"/><path d="M0.6 5h8.8M5 0.6c-2.4 2.6-2.4 6.2 0 8.8M5 0.6c2.4 2.6 2.4 6.2 0 8.8" fill="none" stroke="currentColor" stroke-width="0.8"/></svg>www.voxharbor.example.au</li>
  </ul>
</section>

<section class="card card--tallow" aria-label="Tallowgate business card">
  <svg class="card__art" width="430" height="238" viewBox="0 0 430 238" aria-hidden="true">
    <polygon points="12,124 216,108 216,226 12,214" fill="#0c6fbf"/>
    <polygon points="216,108 418,124 418,214 216,226" fill="#333538"/>
  </svg>
  <div class="brand brand--tallow"><span class="brand__square"></span><span>Tallowgate</span></div>
  <div class="holder">
    <p class="holder__name">Lev Dorrit</p>
    <p class="holder__title">Sales Director</p>
  </div>
  <ul class="contacts">
    <li><svg viewBox="0 0 10 10"><rect x="2.5" y="0.5" width="5" height="9" rx="1" fill="none" stroke="currentColor"/></svg>+61 400 555 187</li>
    <li><svg viewBox="0 0 10 10"><path d="M1 3c0-1 1-2 4-2s4 1 4 2v1H7V3H3v1H1zM2 5h6l1 4H1z"/></svg>+61 3 9555 0137</li>
    <li><svg viewBox="0 0 10 10"><path d="M0 2h10v6H0zM0.8 2.6 5 5.6l4.2-3" fill="none" stroke="currentColor"/></svg>lev@tallowgate.example.au</li>
    <li><svg viewBox="0 0 10 10"><circle cx="5" cy="5" r="4.4" fill="none" stroke="currentColor"/><path d="M0.6 5h8.8M5 0.6c-2.4 2.6-2.4 6.2 0 8.8M5 0.6c2.4 2.6 2.4 6.2 0 8.8" fill="none" stroke="currentColor" stroke-width="0.8"/></svg>www.voxharbor.example.au</li>
  </ul>
</section>

</body>
</html>
```